Makeup artist looking for business card design

- Business card to be memorable and recognisable

- I've attached photos of my logo (File 4), photos that I want to incorporate into the design (File 5,6 & 7) and an example of the design I like "Mirela Stott" (File 1)

- I've attached 3 photos of the designs I want to use, please use one of your choice

- Next to Instagram (File 2) and Facebook (File 3), please use their logo.

- No coloured background, either use the original background (grey) old white.

- Please include the following on the business card:
- Business name: LK Makeup Artistry
- My name: Rosalind Kerr
- Occupation: Makeup Artist
- Contact number: 0437 295 148
- Email: roskerr_makeup@mailvento.com
- Instagram (please use image): @lkmakeupartistry
- Facebook (please use image): www.socialpage.net/LKMakeUpArtistry

Target Market(s)

Target woman for bridal makeup, occasion, fashion makeup and print.

Industry/Entity Type

Business

Requirements
Must have
• Logo provided and photo provided
Should not have
• Colourful background
Too cluttered
Shouldn't use old style font

```html
<!DOCTYPE html>
<html lang="en">
<head>
<meta charset="utf-8">
<title>LK Makeup Artistry – Business Card</title>
<link href="https://fonts.googleapis.com/css2?family=Josefin+Sans:wght@300;400&display=swap" rel="stylesheet">
<style>
  :root {
    --ink: #2b2b2b;
    --ink-soft: #555555;
    --grey-text: #8a8a8a;
    --blush: #d9c2bd;
    --mauve: #a97aa3;
    --card-back: #f1f1f1;
    --stage-top: #ffffff;
    --stage-bottom: #e3c1da;
    --photo-skin: #e9bfae;
    --photo-rose: #d79db0;
    --photo-lilac: #c59ac6;
    --photo-petal: #f3e6f1;
  }
  * { margin: 0; padding: 0; box-sizing: border-box; }
  html, body { width: 1200px; height: 1000px; overflow: hidden; }
  body {
    position: relative;
    font-family: "Josefin Sans", "Helvetica Neue", Arial, sans-serif;
    font-weight: 300;
    color: var(--ink);
    background: linear-gradient(180deg, var(--stage-top) 0%, var(--stage-top) 37%, var(--stage-bottom) 100%);
  }
  .side-label {
    position: absolute;
    top: 34px;
    width: 523px;
    text-align: center;
    font-size: 33px;
    font-weight: 300;
    letter-spacing: 8px;
    color: var(--ink);
  }
  .side-label--front { left: 48px; }
  .side-label--back { left: 604px; }

  .card {
    position: absolute;
    top: 87px;
    width: 523px;
    height: 853px;
    overflow: hidden;
    box-shadow: 0 2px 8px rgba(0,0,0,0.18);
  }
  .card--front { left: 62px; }
  .card--back { left: 609px; background: var(--card-back); }

  .front-photo {
    position: absolute;
    inset: 0;
    background:
      radial-gradient(ellipse 60% 45% at 45% 35%, var(--photo-skin) 0%, rgba(233,191,174,0) 70%),
      radial-gradient(ellipse 55% 60% at 85% 55%, var(--photo-lilac) 0%, rgba(197,154,198,0) 70%),
      linear-gradient(160deg, var(--photo-rose) 0%, var(--photo-skin) 35%, var(--photo-lilac) 65%, var(--photo-petal) 100%);
  }
  .front-brand {
    position: absolute;
    left: 128px;
    top: 790px;
    font-size: 25px;
    font-weight: 300;
    letter-spacing: 2px;
    color: var(--ink);
  }

  .back-brand {
    position: absolute;
    left: 184px;
    top: 298px;
    font-size: 20px;
    font-weight: 300;
    letter-spacing: 1.5px;
    color: var(--ink-soft);
    white-space: nowrap;
  }
  .contact {
    position: absolute;
    right: 26px;
    text-align: right;
    white-space: nowrap;
  }
  .contact__name {
    top: 455px;
    font-size: 44px;
    letter-spacing: 5px;
    color: var(--ink);
    font-weight: 300;
  }
  .contact__role {
    top: 510px;
    font-size: 38px;
    letter-spacing: 13px;
    color: var(--blush);
    right: 13px;
  }
  .contact__phone {
    top: 588px;
    font-size: 30px;
    letter-spacing: 3px;
    color: var(--ink);
  }
  .contact__email {
    top: 633px;
    font-size: 20px;
    letter-spacing: 1.5px;
    color: var(--grey-text);
    text-transform: uppercase;
  }
  .social {
    position: absolute;
    right: 28px;
    display: flex;
    align-items: center;
    gap: 8px;
    font-size: 17px;
    letter-spacing: 1px;
    color: var(--grey-text);
    text-transform: uppercase;
  }
  .social--page { top: 705px; }
  .social--handle { top: 770px; }
  .social__mark {
    width: 52px;
    height: 52px;
    background: var(--mauve);
    border-radius: 4px;
    flex: none;
  }
</style>
</head>
<body>
  <div class="side-label side-label--front">FRONT</div>
  <div class="side-label side-label--back">BACK</div>

  <section class="card card--front">
    <div class="front-photo" role="img" aria-label="Close-up beauty portrait of a model in lilac eye makeup and lipstick beside large purple and white orchid petals"></div>
    <div class="front-brand">LK MAKEUP ARTISTRY</div>
  </section>

  <section class="card card--back">
    <div class="back-brand">LK MAKEUP ARTISTRY</div>
    <div class="contact contact__name">ROSALIND KERR</div>
    <div class="contact contact__role">makeup artist</div>
    <div class="contact contact__phone">0437 295 148</div>
    <div class="contact contact__email">roskerr_makeup@mailvento.com</div>
    <div class="social social--page">
      <span>www.socialpage.net/LKMakeUpArtistry</span>
      <span class="social__mark"></span>
    </div>
    <div class="social social--handle">
      <span>@lkmakeupartistry</span>
      <span class="social__mark"></span>
    </div>
  </section>
</body>
</html>
```